Wine and retail website for a high-end resort community

We are introducing a line of quality wines in the resort community of Tidewater, Massachusetts, USA. The site will detail information about the wine, and online store connected to and external government approved shipper for wine, and additional non-alcoholic retail merchandise sales.

We are planning the site to be driven off the Squarespace platform so I do not believe coding is necessary initially; however, the ability to do sop would be helpful if needed.

Attached are the images/files we have available so far. Please feel free to use stock images in your design.

Target Market(s)

Wine enthusiasts in the resort community of Martha’s Vineyard Massachusetts

Industry/Entity Type

Wine

Number of Pages Required

4 page

Font styles to use
Sans Serif

Requirements
Must have
• Home page, about page, wine page, e-commerce page, retail merchandise page. I recently came across brelmorcellars.com and really like the look and layout of their pages if that helps
Nice to have
• A short wine/Martha’s Vineyard related video on the home page

```html
<!DOCTYPE html>
<html lang="en">
<head>
<meta charset="utf-8">
<title>Tidewater Estates — Discover in Our Wines</title>
<link rel="stylesheet" href="https://fonts.googleapis.com/css2?family=Playfair+Display:wght@400;500&family=Lato:wght@400;700&display=swap">
<style>
:root{
  --black:#0b0b0d;
  --olive:#3f3a27;
  --olive-nav:#4a4229;
  --gold:#c9b13c;
  --gold-text:#c8aa3a;
  --ink:#111111;
  --white:#ffffff;
  --muted:#8e8f94;
  --line:#d9d9d9;
}
*{margin:0;padding:0;box-sizing:border-box}
html,body{width:1200px;height:3998px;overflow:hidden;background:var(--white)}
body{position:relative;font-family:"Lato",Arial,sans-serif;color:var(--ink)}
.abs{position:absolute}
.serif{font-family:"Playfair Display",Georgia,serif;font-weight:400}

/* header */
.topbar{left:0;top:0;width:1200px;height:53px;background:var(--black)}
.nav{left:0;top:53px;width:1200px;height:57px;background:var(--olive-nav)}
.nav a{position:absolute;top:19px;font-size:15px;color:#b9b29a;text-decoration:none}
.nav a.active{color:var(--white);font-weight:700}
.icons{right:36px;top:16px;display:flex;gap:20px}
.brand-box{left:40px;top:14px;width:182px;height:136px;background:var(--white);border-radius:8px;display:flex;flex-direction:column;align-items:center;justify-content:center;z-index:3}
.brand-box .name{font-family:"Playfair Display",Georgia,serif;font-size:28px;line-height:1;color:#333;text-align:center}
.brand-box .mark{width:14px;height:14px;background:#999;border-radius:50%;margin-bottom:10px}

/* hero */
.hero{left:0;top:110px;width:1200px;height:628px;background:linear-gradient(180deg,#1c1a22 0%,#3a3640 40%,#2a2620 75%,#1a1712 100%)}
.hero-text{left:115px;top:255px;width:400px;text-align:center;color:var(--white)}
.hero-text .kicker{font-size:24px;letter-spacing:.5px}
.hero-text h1{font-size:70px;line-height:72px;color:var(--gold);margin-top:4px}
.hero-text p{font-family:"Playfair Display",Georgia,serif;font-size:17px;line-height:25px;margin-top:14px}
.btn{position:absolute;display:flex;align-items:center;justify-content:center;font-size:19px;color:var(--ink);background:var(--gold);text-decoration:none}
.btn.outline{background:transparent;border:2px solid var(--gold);color:var(--white)}

/* sections */
.photo{position:absolute}
.sig{position:absolute;width:252px;height:70px;background:linear-gradient(90deg,#f1f1f1,#e4e4e4)}
.label{position:absolute;border:2px solid #cfcfcf;background:linear-gradient(180deg,#ffffff 0%,#f6f6f6 55%,#dedede 100%)}
.body-text{font-size:12.5px;line-height:17px;color:#222}
h2.big{font-size:58px;line-height:1}
h3.wine{font-size:38px;line-height:1.1}
.region{font-family:"Playfair Display",Georgia,serif;font-size:25px;margin-top:6px}
.band{position:absolute;background:var(--olive)}
.band .gold{color:var(--gold-text)}
.band .light{color:#eeeae0}
.field{left:45px;top:3643px;width:1110px;height:62px;border:1px solid #eeeeee;box-shadow:0 1px 3px rgba(0,0,0,.06)}
.footer{left:0;top:3764px;width:1200px;height:234px;background:var(--black);color:var(--white)}
.footer .links a{position:absolute;top:162px;font-size:12px;color:#d0d0d0;text-decoration:none}
.socials{left:520px;top:156px;display:flex;gap:30px}
.socials span{width:18px;height:18px;border:2px solid #fff;border-radius:50%}
</style>
</head>
<body>

<header>
  <div class="abs topbar"></div>
  <div class="abs icons">
    <svg width="20" height="20" viewBox="0 0 20 20" fill="none" stroke="#fff" stroke-width="2"><circle cx="8" cy="8" r="6"/><path d="M13 13l5 5"/></svg>
    <svg width="20" height="20" viewBox="0 0 20 20" fill="none" stroke="#fff" stroke-width="2"><circle cx="10" cy="6" r="4"/><path d="M3 19c1-5 13-5 14 0"/></svg>
    <svg width="22" height="20" viewBox="0 0 22 20" fill="none" stroke="#fff" stroke-width="2"><path d="M1 2h3l3 11h11l2-8H6"/><circle cx="9" cy="17" r="1.5"/><circle cx="16" cy="17" r="1.5"/></svg>
  </div>
  <nav class="abs nav">
    <a class="active" href="#" style="left:405px">Home</a>
    <a href="#" style="left:524px">About</a>
    <a href="#" style="left:624px">Shop</a>
    <a href="#" style="left:730px">Contact</a>
  </nav>
  <div class="abs brand-box">
    <span class="mark"></span>
    <span class="name">Tidewater<br>Estates</span>
  </div>
</header>

<section class="abs hero" role="img" aria-label="Night sky over a lighthouse and grassy dunes with a bottle of red and a bottle of white wine"></section>
<div class="abs hero-text">
  <div class="kicker">TASTE OUR WINES</div>
  <h1 class="serif">Discover in Our Wines</h1>
  <p>Everyone will find something very own in our outstanding wines. Don't miss the chance.</p>
</div>
<a class="btn" href="#" style="left:216px;top:515px;width:180px;height:57px">Discover</a>

<section>
  <div class="photo" role="img" aria-label="Man tasting red wine from a glass" style="left:0;top:738px;width:550px;height:504px;background:linear-gradient(90deg,#1a1a1a 0%,#3a2a24 50%,#e9e4e0 90%,#ffffff 100%)"></div>
  <div class="abs" style="left:610px;top:835px;width:540px">
    <div class="serif" style="font-size:28px">A New Generation of</div>
    <h2 class="serif big" style="margin-top:18px">Winemakers</h2>
    <p class="body-text" style="margin-top:14px;text-align:justify">Lorem ipsum dolor sit amet, consectetuer adipiscing elit. Aenean commodo ligula eget dolor. Aenean massa. Cum sociis natoque penatibus et magnis dis parturient montes, nascetur ridiculus mus. Lorem ipsum dolor sit amet, consectetur adipiscing elit. Curabitur sit amet elit leo.</p>
    <p class="body-text" style="margin-top:24px;text-align:justify">Cras dapibus. Vivamus elementum semper nisi. Aenean vulputate eleifend tellus. Aenean leo ligula, porttitor eu, consequat vitae, eleifend ac, enim. Aliquam lorem ante, dapibus in, viverra quis, feugiat a, tellus. .</p>
  </div>
  <div class="sig" role="img" aria-label="Handwritten winemaker signature" style="left:610px;top:1160px"></div>
</section>

<section>
  <div class="photo" role="img" aria-label="Silhouette map of the island" style="left:57px;top:1325px;width:104px;height:60px;background:#111;border-radius:30px 20px 12px 8px"></div>
  <div class="abs" style="left:57px;top:1405px;width:460px">
    <h3 class="serif wine">Cabernet Sauvignon</h3>
    <div class="region">California</div>
    <p class="body-text" style="margin-top:14px">Tidewater Estates Cabernet Sauvignon shows aromas of oak, baking spice, and cassis. On the palate, tones of black cherry and a hint of cinnamon, nutmeg and French Vanilla leave a delicious lasting finish.</p>
    <p class="body-text" style="margin-top:20px">We hope our wines are a reminder of good times and good company spent on the island. Here's to keeping it on island time!</p>
    <p class="body-text" style="margin-top:30px;font-size:12px">Cheers,</p>
  </div>
  <div class="sig" role="img" aria-label="Handwritten winemaker signature" style="left:57px;top:1685px"></div>
  <div class="label" role="img" aria-label="Cabernet Sauvignon 2022 bottle label with a faded coastal lighthouse scene" style="left:657px;top:1312px;width:388px;height:438px"></div>
</section>

<section>
  <div class="photo" role="img" aria-label="Close-up of a Cabernet Sauvignon bottle and a Chardonnay bottle" style="left:45px;top:1803px;width:562px;height:600px;background:linear-gradient(120deg,#1b1b1b 0%,#d9d7d2 35%,#2a2a22 55%,#e4ddc0 75%,#b6a03f 100%)"></div>
  <div class="band" style="left:607px;top:1803px;width:548px;height:600px">
    <div class="abs" style="left:53px;top:60px;width:460px">
      <div class="serif light" style="font-size:40px;line-height:1">2022</div>
      <div class="serif light" style="font-size:20px;margin-top:6px">CURRENT RELEASE</div>
      <h3 class="serif wine gold" style="margin-top:12px">Cabernet Sauvignon</h3>
      <p class="body-text light" style="margin-top:12px">Tidewater Estates Cabernet Sauvignon shows aromas of oak, baking spice, and cassis. On the palate, tones of black cherry and a hint of cinnamon, nutmeg and French Vanilla leave a delicious lasting finish.</p>
      <h3 class="serif wine gold" style="margin-top:40px">Chardonnay</h3>
      <p class="body-text light" style="margin-top:12px">Tidewater Estates Chardonnay is defined by an array of fragrant fruit with buttery undertones that finish long and smooth. A true classic that is sure to please any palate.</p>
    </div>
    <a class="btn" href="#" style="left:50px;top:471px;width:178px;height:49px">Discover</a>
    <a class="btn outline" href="#" style="left:243px;top:471px;width:178px;height:49px">View All</a>
  </div>
</section>

<section>
  <div class="abs" style="left:57px;top:2472px;width:440px">
    <h3 class="serif wine">Chardonnay</h3>
    <div class="region" style="margin-top:0">California</div>
    <p class="body-text" style="margin-top:30px">Tidewater Estates Chardonnay is defined by an array of fragrant fruit with buttery undertones that finish long and smooth. A true classic that is sure to please any palate.</p>
    <p class="body-text" style="margin-top:12px">We hope our wines are a reminder of good times and good company spent on the island. Here's to keeping it on island time!</p>
    <p class="body-text" style="margin-top:64px;font-weight:700;font-size:15px">Cheers,</p>
  </div>
  <div class="sig" role="img" aria-label="Handwritten winemaker signature" style="left:57px;top:2785px"></div>
  <div class="label" role="img" aria-label="Chardonnay 2022 bottle label with a faded coastal scene" style="left:652px;top:2452px;width:408px;height:403px"></div>
</section>

<section>
  <div class="band" style="left:45px;top:2907px;width:560px;height:607px">
    <div class="abs" style="left:40px;top:128px;width:480px;text-align:center">
      <div class="light" style="font-size:15px;font-weight:700">THE ESTATE</div>
      <div class="serif light" style="font-size:36px;margin-top:6px">Tasting &amp; Tours</div>
      <p class="light" style="font-size:13.5px;line-height:28px;margin:36px auto 0;width:360px">Lorem ipsum dolor sit amet, consectetur adipiscing. Cras vel iaculis urna. Cras bibendum ex id dolor facilisis, in tempor lacus dapibus.</p>
    </div>
    <a class="btn" href="#" style="left:189px;top:427px;width:180px;height:49px">Read More</a>
  </div>
  <div class="photo" role="img" aria-label="Red wine being poured into a glass" style="left:605px;top:2907px;width:550px;height:607px;background:linear-gradient(135deg,#3a3020 0%,#d8c9a0 35%,#f4efe6 55%,#9e1e24 78%,#e3c37a 100%)"></div>
</section>

<section>
  <div class="abs" style="left:0;top:3562px;width:1200px;text-align:center">
    <div style="font-size:14px;font-weight:700">BE CONNECTED</div>
    <div class="serif" style="font-size:36px;line-height:1.1">Join Our Club</div>
  </div>
  <div class="abs field">
    <span class="abs" style="left:26px;top:24px;font-size:12px;color:#bbb">Email Address</span>
    <span class="abs" style="right:30px;top:23px;font-size:13px">Sign Up</span>
  </div>
</section>

<footer class="abs footer">
  <div class="abs" style="left:0;top:36px;width:1200px;text-align:center">
    <div style="font-size:15px;font-weight:700">TIDEWATER PROMISE</div>
    <div class="serif" style="font-size:36px;margin-top:8px">We Make Good Wines</div>
  </div>
  <div class="links">
    <a href="#" style="left:42px">FAQ</a>
    <a href="#" style="left:104px">TERMS</a>
    <a href="#" style="left:190px">PRIVACY</a>
    <a href="#" style="left:288px">RETURNS</a>
  </div>
  <div class="abs socials"><span></span><span></span><span></span><span></span></div>
  <div class="abs" style="right:42px;top:162px;font-size:12px;color:#d0d0d0">© 2024 TIDEWATER ESTATES . ALL RIGHTS RESERVED</div>
</footer>

</body>
</html>
```